Classroom Stewards Certificate - Word Template

We need a MS Word certificate template for the Lanternhouse 9 Classroom Stewards program. We are global non-profit that connects artists, educators, and students through the power of art and education. The final design should be fun and vibrant, yet professional. It shoud also include the program logo and feature the L9 purple (see brand guidelines).

Our brand guidelines are here: https://stylekitbox.example/lanternhouse-9 and I've uploaded the program logo.

```html
<!DOCTYPE html>
<html lang="en">
<head>
<meta charset="utf-8">
<title>CEU Certificate – Lanternhouse 9 Classroom Stewardship</title>
<link rel="stylesheet" href="https://fonts.googleapis.com/css2?family=Marcellus&family=Montserrat:wght@700&family=Cormorant+Garamond:ital,wght@1,400;1,600;1,700&family=Arimo&display=swap">
<style>
  :root {
    --l9-purple: #5b3aa6;
    --purple-soft: #b7a8dc;
    --paper: #fbfbfa;
    --border-grey: #e4e4e6;
    --ink: #2b2b2b;
    --ink-soft: #5a5a5a;
    --ribbon: #2e2e2e;
  }
  * { box-sizing: border-box; margin: 0; padding: 0; }
  html, body { width: 1200px; height: 801px; overflow: hidden; background: #dcdde0; }
  .certificate {
    position: relative; width: 1200px; height: 801px;
    background: var(--paper); color: var(--ink);
    font-family: "Cormorant Garamond", Georgia, serif;
  }
  .ornament-band { position: absolute; inset: 0; background: var(--border-grey); }
  .frame { position: absolute; inset: 0; }
  .content { position: absolute; inset: 0; text-align: center; }

  .brand { position: absolute; top: 92px; left: 0; right: 0; display: flex; justify-content: center; align-items: center; gap: 10px; }
  .brand-dot { width: 18px; height: 18px; border-radius: 50%; background: var(--l9-purple); }
  .brand-name { font-family: "Marcellus", serif; color: var(--l9-purple); font-size: 20px; letter-spacing: 1px; }

  .title { position: absolute; top: 132px; left: 0; right: 0; font-family: "Marcellus", serif; font-weight: 400; font-size: 58px; letter-spacing: 6px; color: var(--ink); }
  .subtitle { position: absolute; top: 212px; left: 0; right: 0; display: flex; justify-content: center; align-items: center; gap: 14px; }
  .subtitle-text { font-family: "Montserrat", sans-serif; font-weight: 700; font-size: 15px; letter-spacing: 3px; color: var(--l9-purple); }
  .subtitle-rule { width: 90px; height: 5px; border-top: 1px solid var(--purple-soft); border-bottom: 1px solid var(--purple-soft); }

  .topic-ribbon { position: absolute; top: 248px; left: 50%; transform: translateX(-50%); width: 620px; height: 34px; display: flex; align-items: center; }
  .ribbon-cap { width: 22px; height: 34px; background: var(--ribbon); }
  .ribbon-cap.left { border-radius: 17px 0 0 17px; }
  .ribbon-cap.right { border-radius: 0 17px 17px 0; }
  .ribbon-body { flex: 1; height: 26px; border: 1px solid var(--ink); margin: 0 4px; display: flex; align-items: center; justify-content: center; font-family: "Marcellus", serif; font-size: 14px; letter-spacing: 1.5px; }

  .fill-line { display: inline-block; border-bottom: 1px solid var(--ink); height: 1px; vertical-align: 4px; }
  .statement { position: absolute; left: 150px; right: 150px; font-style: italic; font-size: 24px; text-align: left; display: flex; align-items: baseline; gap: 8px; }
  .statement .fill-line { flex: 1; }
  .statement-1 { top: 310px; }
  .statement-2 { top: 352px; }

  .details { position: absolute; top: 402px; left: 170px; right: 170px; font-style: italic; font-size: 13.5px; line-height: 1.35; color: var(--ink-soft); }
  .details p + p { margin-top: 7px; }

  .certified { position: absolute; top: 608px; left: 0; right: 0; font-style: italic; font-weight: 700; font-size: 22px; }
  .signature { position: absolute; top: 664px; left: 50%; transform: translateX(-50%); width: 300px; border-top: 1px solid var(--ink); padding-top: 4px; font-family: "Arimo", sans-serif; font-size: 13px; line-height: 1.3; color: var(--ink-soft); }
</style>
</head>
<body>
<main class="certificate">
  <div class="ornament-band" role="img" aria-label="Ornamental purple border of chain links and corner flourishes"></div>

  <svg class="frame" width="1200" height="801" viewBox="0 0 1200 801" aria-hidden="true">
    <path d="M90 58 H1110 A32 32 0 0 0 1142 90 V711 A32 32 0 0 0 1110 743 H90 A32 32 0 0 0 58 711 V90 A32 32 0 0 0 90 58 Z" fill="var(--paper)"/>
    <path d="M90 58 H1110 A32 32 0 0 0 1142 90 V711 A32 32 0 0 0 1110 743 H90 A32 32 0 0 0 58 711 V90 A32 32 0 0 0 90 58 Z" fill="none" stroke="var(--l9-purple)" stroke-width="7"/>
    <path d="M98 70 H1102 A28 28 0 0 0 1130 98 V703 A28 28 0 0 0 1102 731 H98 A28 28 0 0 0 70 703 V98 A28 28 0 0 0 98 70 Z" fill="none" stroke="var(--l9-purple)" stroke-width="2"/>
  </svg>

  <section class="content">
    <div class="brand"><span class="brand-dot"></span><span class="brand-name">Lanternhouse 9</span></div>
    <h1 class="title">CEU CERTIFICATE</h1>
    <div class="subtitle">
      <span class="subtitle-rule"></span>
      <span class="subtitle-text">L9 CLASSROOM STEWARDSHIP</span>
      <span class="subtitle-rule"></span>
    </div>
    <div class="topic-ribbon">
      <span class="ribbon-cap left"></span>
      <span class="ribbon-body">SOCIOEMOTIONAL LEARNING, NARRATIVE, LISTENING AND SPEAKING</span>
      <span class="ribbon-cap right"></span>
    </div>

    <p class="statement statement-1">This certifies that <span class="fill-line"></span> Participated in a series of professional</p>
    <p class="statement statement-2">development experiences from <span class="fill-line"></span> To <span class="fill-line"></span>.</p>

    <div class="details">
      <p>The educator learned how to run the L9 Tale Swap in live and virtual environments. The Tale Swap method is designed to help students understand that their voices, stories, actions and lives matter. It is a research-proven method to foster empathy and support students' positive identity building through personal narrative. The educator has now achieved certification as an L9 Tale Swap Facilitator.</p>
      <p>This means that they have the tools to: Build a safe space through communication; Model and provide explicit teaching around listening; Navigate challenges in group dynamics; Manage the pair and share technique; Explain research on empathy and storytelling; Debrief about feelings, impacts, and lessons from the Tale Swap experience; Address their own feelings during and after the Tale Swap.</p>
      <p>In addition, the educator has done the following curriculum work: Conducted the Tale Swap in their school; Collaborated with other teachers across the country to create curriculum connected to the Tale Swap and English Language Arts standards.</p>
      <p>As a result, the individual above should receive 6 continuing education units (CEUs) for 60 contact hours.</p>
    </div>

    <p class="certified">Certified by:</p>
    <div class="signature">
      Helena Marsh<br>Director of Learning Resources<br>Lanternhouse 9
    </div>
  </section>
</main>
</body>
</html>
```